Stationery Design Project

Our company is "Meridal Systems" and we have a product called "quillbrook.com". The product is an online accounting software for businesses. We want to communicate that our software will help business owners to be more efficient and help them track their finances better. Quillbrook.com is basically a simple version of ledgerpine.

"We want a unique and creative design which will surprise our customer."

NAME CARD = QUILLBROOK
We want a quillbrook name card NOT MERIDAL SYSTEMS.

For the content of the name card, please make sure it fit with a long name like the following:

Roswin Halim Alias Roswin
Developer Specialist
T: (021) 4172 3846
F: (021) 4172 3847
E: customer.service@mrd.co.id

I need you to put it the following information to the name card

"quillbrook"
- moto is "automate your businesses"
- website "www.quillbrook.com"
- quillbrook is a "Web Accounting Software"
- product of "Meridal Systems"

LETTERHEAD, ENVELOPE, FOLDER = MERIDAL SYSTEMS
Other than name card we wanted you to design for us; letterhead, envelope and folder. In letterhead, envelope and folder it should ONLY contain the following information ("Meridal Systems").
PLEASE BE SURE YOU ARE NOT PUTTING "QUILLBROOK LOGO" IN LETTERHEAD, ENVELOPE AND FOLDER.

"Meridal Systems"
Address:
Ruko Harbor Plaza Blok. D No. 18
Jl. Kembangsari No. 47
Jakarta
Kalideres, 11840
Indonesia

Web Address: mrd.co.id

T: (021) 4172 3846
F: (021) 4172 3847

Target Market(s)

Business Owners, Accountant, Auditor, Tax Consultant

Industry/Entity Type

Accounting

Requirements
Must have
• .

```html
<!DOCTYPE html>
<html lang="en">
<head>
<meta charset="utf-8">
<title>Meridal Systems – Envelope</title>
<link href="https://fonts.googleapis.com/css2?family=Alegreya+Sans:wght@400;500&family=Tenor+Sans&display=swap" rel="stylesheet">
<style>
  :root {
    --canvas: #ffffff;
    --edge: #b9b9b9;
    --green-deep: #1c3510;
    --green-mid: #4fae0a;
    --green-lime: #c6ff00;
    --ink: #4b5a5c;
    --paper-text: #ffffff;
  }
  html, body {
    margin: 0;
    padding: 0;
    width: 1200px;
    height: 900px;
    overflow: hidden;
    background: var(--canvas);
  }
  .sheet {
    position: relative;
    width: 1200px;
    height: 900px;
  }
  .envelope {
    position: absolute;
    left: 262px;
    width: 678px;
    height: 301px;
    box-sizing: border-box;
    border: 1px solid var(--edge);
    background: var(--canvas);
    overflow: hidden;
  }
  .envelope--front { top: 99px; }
  .envelope--back { top: 501px; }

  .front__band {
    position: absolute;
    left: -1px;
    top: -1px;
    width: 62px;
    height: 301px;
    background: linear-gradient(to bottom, var(--green-deep) 0%, var(--green-mid) 50%, var(--green-lime) 100%);
  }
  .brand {
    position: absolute;
    left: 86px;
    top: 29px;
    display: flex;
    align-items: center;
    gap: 8px;
  }
  .brand__dot {
    width: 46px;
    height: 46px;
    border-radius: 50%;
    background: var(--green-mid);
  }
  .brand__name {
    font-family: "Alegreya Sans", sans-serif;
    font-weight: 500;
    font-size: 18px;
    letter-spacing: 0.5px;
    color: var(--ink);
  }
  .tagline {
    position: absolute;
    right: 27px;
    top: 40px;
    margin: 0;
    font-family: "Tenor Sans", sans-serif;
    font-size: 15px;
    font-variant: small-caps;
    letter-spacing: 5px;
    color: var(--ink);
  }

  .back__flap {
    position: absolute;
    left: -1px;
    top: -1px;
    width: 678px;
    height: 130px;
  }
  .return-address {
    position: absolute;
    left: 0;
    right: 0;
    top: 33px;
    margin: 0;
    text-align: center;
    font-family: "Alegreya Sans", sans-serif;
    font-style: normal;
    font-size: 13.5px;
    line-height: 12px;
    color: var(--paper-text);
  }
</style>
</head>
<body>
<main class="sheet">
  <section class="envelope envelope--front" aria-label="Envelope front">
    <div class="front__band"></div>
    <div class="brand">
      <span class="brand__dot"></span>
      <span class="brand__name">MERIDAL SYSTEMS</span>
    </div>
    <p class="tagline">Simplify Work</p>
  </section>

  <section class="envelope envelope--back" aria-label="Envelope back">
    <svg class="back__flap" viewBox="0 0 678 130" xmlns="http://www.w3.org/2000/svg" aria-hidden="true">
      <defs>
        <linearGradient id="flapGradient" x1="0" y1="0" x2="0" y2="1">
          <stop offset="0" stop-color="#1c3510"/>
          <stop offset="0.5" stop-color="#4fae0a"/>
          <stop offset="1" stop-color="#c6ff00"/>
        </linearGradient>
      </defs>
      <path d="M0,0 L678,0 L670,49 Q339,199 8,49 Z" fill="url(#flapGradient)"/>
    </svg>
    <address class="return-address">
      Ruko Harbor Plaza Blok D No. 18<br>
      Jl. Kembangsari No. 47<br>
      Jakarta<br>
      Kalideres, 11840<br>
      Indonesia<br>
      Web Address: mrd.co.id
    </address>
  </section>
</main>
</body>
</html>
```